Flyer for the Harvest of lanterns conference

Flyer design for an annual international conference called "MERIVAL 2017". This is a conference for young adults, so we hope to produce a design that is both professional and appealing to young people in general

We'd like the flyer to showcase the conference brand logo, and clearly highlight the key information to people who will read it.

Target Market(s)

Young people, young adults

Industry/Entity Type

Religious

Font styles to use
Sans Serif

Colors

Designer to choose colors to be used in the design.

Requirements
Must have
• - Should be only one page (Vertical or Horizontal).
• - the MERVAL logo and all the information found in the attached text file. This includes: Main topic: Your sons and daughters shall prophesy,
• Dates and time, location, contact information and everything that is in the attached text file.
Nice to have
• It would be nice to see samples where the white logo is used and another where the black one is used.
Should not have
• This is NOT a folded flyer, we will be sticking it on doors and public places. And we will be printing large simple to put on walls. So only one page with few words like an add (the words are in the attached file)

```html
<!DOCTYPE html>
<html lang="en">
<head>
<meta charset="utf-8">
<title>MERIVAL 2017 — Harvest of Lanterns Conference</title>
<link rel="stylesheet" href="https://fonts.googleapis.com/css2?family=Roboto+Condensed:wght@400;700&family=Roboto:wght@400;500;700&display=swap">
<style>
  :root {
    --navy: #24223f;
    --charcoal: #2f2e2e;
    --orange: #ef7f1a;
    --white: #ffffff;
    --logo-grey: #e9e9e9;
    --ink: #2a2a2a;
    --page-bg: #ece6dc;
  }
  * { margin: 0; padding: 0; box-sizing: border-box; }
  html, body { width: 1020px; height: 1200px; overflow: hidden; }
  body { background: var(--page-bg); font-family: "Roboto", Arial, sans-serif; }

  .flyer {
    position: absolute; left: 99px; top: 20px;
    width: 822px; height: 1160px;
    background: var(--white); overflow: hidden;
  }

  .hero-photo {
    position: absolute; left: 0; top: 0; width: 822px; height: 311px;
    background:
      radial-gradient(ellipse 220px 160px at 390px 150px, #f6d39a 0%, rgba(246,190,120,0) 100%),
      linear-gradient(180deg, #e48a58 0%, #e79a66 45%, #c86a4a 75%, #3c2f52 100%);
  }

  .title-band {
    position: absolute; left: 0; top: 311px; width: 822px; height: 172px;
    background: var(--navy);
  }
  .event-title {
    position: absolute; left: 42px; top: 30px;
    font-family: "Roboto Condensed", "Arial Narrow", sans-serif;
    font-weight: 700; font-size: 75px; line-height: 1; color: var(--white);
    letter-spacing: 1px;
  }
  .event-subtitle {
    position: absolute; left: 44px; top: 104px;
    font-family: "Roboto Condensed", "Arial Narrow", sans-serif;
    font-weight: 700; font-size: 28px; color: var(--orange); text-transform: uppercase;
  }
  .brand-box {
    position: absolute; left: 580px; top: 0; width: 190px; height: 172px;
    background: var(--logo-grey);
    display: flex; flex-direction: column; align-items: center; justify-content: center; gap: 12px;
  }
  .brand-mark { width: 62px; height: 62px; border-radius: 50%; background: var(--orange); }
  .brand-name {
    font-family: "Roboto", Arial, sans-serif; font-weight: 500; font-size: 28px;
    color: var(--ink); letter-spacing: 1px;
  }

  .theme {
    position: absolute; left: 0; top: 483px; width: 822px; height: 111px;
  }
  .theme-line {
    position: absolute; left: 50px; top: 38px; width: 722px;
    font-family: "Roboto Condensed", "Arial Narrow", sans-serif;
    font-weight: 700; font-size: 34px; color: var(--orange);
    text-align: center; text-transform: uppercase;
    padding-bottom: 10px; border-bottom: 2px solid var(--orange);
  }

  .details {
    position: absolute; left: 0; top: 594px; width: 822px; height: 324px;
    background: var(--charcoal);
  }
  .speakers-label {
    position: absolute; left: 149px; top: 38px;
    border: 1px solid var(--white); color: var(--white);
    font-size: 18px; padding: 3px 12px; letter-spacing: 0.5px;
  }
  .speaker-list {
    position: absolute; left: 83px; top: 94px; list-style: none;
  }
  .speaker-list li {
    color: var(--white); font-weight: 700; font-size: 15px; line-height: 1;
    margin-bottom: 30px; display: flex; align-items: center;
  }
  .speaker-list li::before {
    content: ""; width: 9px; height: 9px; border-radius: 50%;
    background: var(--orange); margin-right: 16px;
  }
  .divider { position: absolute; left: 397px; top: 28px; }

  .date-card {
    position: absolute; left: 467px; top: 36px; width: 312px; height: 266px;
    background: var(--orange); padding: 13px;
  }
  .date-card-inner {
    width: 100%; height: 100%; border: 1.5px dashed rgba(255,255,255,0.8);
    display: flex; flex-direction: column; align-items: center; justify-content: center;
    color: var(--white); text-align: center; line-height: 1.22;
  }
  .date-days { font-weight: 700; font-size: 28px; }
  .date-month, .start-label { font-size: 33px; font-weight: 400; }
  .date-year, .start-time { font-weight: 700; font-size: 30px; }

  .venue {
    position: absolute; left: 0; top: 918px; width: 822px; height: 192px; text-align: center;
  }
  .room {
    position: absolute; left: 0; top: 8px; width: 822px;
    font-family: "Roboto Condensed", "Arial Narrow", sans-serif;
    font-weight: 700; font-size: 45px; line-height: 1.2; color: var(--ink);
  }
  .room-label { color: var(--orange); }
  .location-box {
    position: absolute; left: 229px; top: 84px; width: 364px; height: 94px;
    border: 1.5px solid var(--orange);
    display: flex; flex-direction: column; justify-content: flex-start;
    padding-top: 22px;
    font-style: normal; font-size: 17px; line-height: 1.3; color: var(--ink);
  }
  .location-title {
    position: absolute; left: 50%; top: 64px; transform: translateX(-50%);
    background: var(--white); padding: 0 8px;
    font-family: "Roboto Condensed", "Arial Narrow", sans-serif;
    font-weight: 700; font-size: 36px; line-height: 1; color: var(--orange);
  }

  .contact-bar {
    position: absolute; left: 0; top: 1110px; width: 822px; height: 50px;
    background: var(--orange);
  }
  .phone-panel {
    position: absolute; left: 0; top: 0; width: 420px; height: 50px;
    background: var(--charcoal);
    clip-path: polygon(0 0, 100% 0, 96% 100%, 0 100%);
    display: flex; align-items: center; padding-left: 58px; gap: 12px;
    color: var(--white);
    font-family: "Roboto Condensed", "Arial Narrow", sans-serif;
    font-weight: 700; font-size: 32px;
  }
  .online {
    position: absolute; left: 448px; top: 0; height: 50px;
    display: flex; align-items: center; color: var(--white); font-size: 13px;
  }
  .online-item { display: flex; align-items: center; gap: 8px; }
  .online-item::before {
    content: ""; width: 9px; height: 9px; border-radius: 50%;
    border: 2px solid var(--white);
  }
  .online-sep { width: 1px; height: 26px; background: rgba(255,255,255,0.7); margin: 0 22px; }
</style>
</head>
<body>
<main class="flyer">
  <div class="hero-photo" role="img" aria-label="Silhouetted crowd raising hands and crosses against an orange sunset sky"></div>

  <header class="title-band">
    <h1 class="event-title">MERIVAL 2017</h1>
    <p class="event-subtitle">Harvest of lanterns Conference</p>
    <div class="brand-box">
      <span class="brand-mark"></span>
      <span class="brand-name">MERVAL</span>
    </div>
  </header>

  <section class="theme">
    <h2 class="theme-line">Your sons and daughters shall prophesy</h2>
  </section>

  <section class="details">
    <p class="speakers-label">OUR SPEAKERS</p>
    <ul class="speaker-list">
      <li>PROPHET LUCIEN MOREAU</li>
      <li>BISHOP SAMUEL NDAYE</li>
      <li>PROPHET JOEL MBUYI TANGA</li>
      <li>PROPHET ANDRE KILOLO</li>
      <li>PROPHET MARC LUTETE</li>
    </ul>
    <svg class="divider" width="20" height="270" viewBox="0 0 20 270" aria-hidden="true">
      <line x1="1" y1="0" x2="1" y2="270" stroke="#ffffff" stroke-opacity="0.6" stroke-width="1.5"/>
      <polygon points="1,127 14,135 1,143" fill="#ffffff"/>
    </svg>
    <div class="date-card">
      <div class="date-card-inner">
        <span class="date-days">1st, 2nd and 3rd</span>
        <span class="date-month">SEPTEMBER</span>
        <span class="date-year">2017</span>
        <span class="start-label">START TIME</span>
        <span class="start-time">6:00PM</span>
      </div>
    </div>
  </section>

  <section class="venue">
    <p class="room"><span class="room-label">Room:</span> Driftwood Ballroom</p>
    <address class="location-box">
      <span>Harborview Lodge &amp; Suites</span>
      <span>418 Ocean Avenue</span>
      <span>Westbrook, ME 04092 United States</span>
    </address>
    <p class="location-title">LOCATION</p>
  </section>

  <footer class="contact-bar">
    <div class="phone-panel">
      <svg width="28" height="28" viewBox="0 0 24 24" aria-hidden="true">
        <path d="M6.6 10.8c1.4 2.8 3.8 5.1 6.6 6.6l2.2-2.2c.3-.3.7-.4 1-.2 1.1.4 2.3.6 3.6.6.6 0 1 .4 1 1V20c0 .6-.4 1-1 1C10.6 21 3 13.4 3 4c0-.6.4-1 1-1h3.5c.6 0 1 .4 1 1 0 1.3.2 2.5.6 3.6.1.3 0 .7-.2 1z" fill="none" stroke="#ffffff" stroke-width="1.6"/>
      </svg>
      <span>+1 (207) 555 0148</span>
    </div>
    <div class="online">
      <span class="online-item">hello@mervalconf.org</span>
      <span class="online-sep"></span>
      <span class="online-item">www.mervalconf.org</span>
    </div>
  </footer>
</main>
</body>
</html>
```